Magazine Design Project

Our company Villa Sorbetto Nero - www.villasorbettonero.co.uk

Villa Sorbetto Nero has been established for three years and produce artisan gelato from fresh ingredients on a wholesale scale. We also cater for weddings and parties.
We supply in scoop cups, ready to scoop pans and can arrange a display freezer of 10 flavours with staff to scoop for guests.

We need a A4 full spread Magazine Advertisement (with 5mm border from the edge of the page) for a Gelato wholesaling business. It'll be advertised in a local community Indian arts magazine so needs to be eyecatching with colourful images boasting handmade artisan gelato. Most readers of this magazine will be of indian origin and self employed business owners looking for new ideas and oppurtunities and will be viewing events and productions organised by the arts company.

We pride ourselves with our inventive flavours and exceptional prices.

We would like to see designs showing colourful pans of gelato, details of what we sell and still maintaining an image of premium, quality and an authentic italian product.

Target Market(s)

Ages 20-60, Male & Female, All education levels, Self Employed who are looking to introduce this product in their food business,

Industry/Entity Type

Events

Requirements
Must have
• The design must be one A4 page and use the logo on the first page of the document we have attached - the border around the logo can be ommitted as we have done on our website www.villasorbettonero.co.uk
Nice to have
• Bold colours, artisan gelato images and an authentic Italian feel
Should not have
• Should not look like it appeals to children or have images of standard ice cream cones. Avoid putting cost list on the advertisement

```html
<!DOCTYPE html>
<html lang="en">
<head>
<meta charset="utf-8">
<title>Villa Sorbetto Nero – Magazine Advertisement</title>
<link href="https://fonts.googleapis.com/css2?family=Cinzel:wght@400;500&family=Crimson+Text:ital,wght@0,400;1,400;1,700&family=Open+Sans:ital,wght@0,400;0,700;1,700&display=swap" rel="stylesheet">
<style>
  :root{
    --page-bg:#e6e1d9;
    --paper:#ffffff;
    --cocoa:#4a2a1a;
    --cocoa-deep:#33201a;
    --berry-red:#b3261c;
    --band-red:#a8261d;
    --cream:#efe3c8;
    --cream-edge:#e2d0aa;
    --mango:#f4b21c;
    --lemon:#f7e7a0;
    --ink:#2f2119;
    --white:#ffffff;
  }
  *{box-sizing:border-box;margin:0;padding:0}
  html,body{width:931px;height:1200px;overflow:hidden;background:var(--page-bg)}
  .advert{
    position:absolute;left:42px;top:0;width:847px;height:1200px;
    background:var(--paper);overflow:hidden;
    font-family:"Open Sans",Arial,sans-serif;color:var(--ink);
  }
  .hero-photo{
    position:absolute;right:0;top:0;width:560px;height:560px;
    background:radial-gradient(ellipse at 70% 35%,#fbf6e6 0%,#f7e9b8 30%,#f3d36e 48%,rgba(255,255,255,0) 72%);
    opacity:.75;
  }
  .brand{position:absolute;left:0;right:0;top:30px;text-align:center}
  .brand-mark{display:flex;align-items:center;justify-content:center;gap:12px;margin-top:78px}
  .brand-dot{width:22px;height:22px;border-radius:50%;background:var(--cocoa)}
  .brand-name{font-family:"Crimson Text",Georgia,serif;font-size:38px;color:var(--cocoa);font-weight:400}
  .brand-tagline{font-family:"Crimson Text",Georgia,serif;font-size:17px;color:var(--cocoa);margin-top:6px}
  .headline{
    position:absolute;left:0;right:0;top:268px;text-align:center;
    font-family:"Cinzel",Georgia,serif;font-size:58px;font-weight:400;color:var(--cocoa);letter-spacing:1px;
  }
  .gallery{position:absolute;left:45px;top:369px;width:761px;height:155px;display:flex;gap:6px}
  .gallery-photo{flex:1;border:3px solid var(--cocoa-deep);border-radius:10px}
  .gallery-photo.display-case{background:linear-gradient(135deg,#e3a23a,#c9462e 45%,#f0e2c2)}
  .gallery-photo.flavour-pans{background:linear-gradient(135deg,#c9c08a,#f1ec9a 40%,#d0463e 75%,#e8e0cc)}
  .gallery-photo.scoops{background:linear-gradient(135deg,#f29a3b,#f07aa0 45%,#8fd07a 80%,#6a3b22)}
  .catering-band{
    position:absolute;left:0;top:556px;width:847px;height:44px;background:var(--band-red);
    color:var(--white);font-family:"Cinzel",Georgia,serif;font-size:29px;text-align:center;line-height:44px;
  }
  .offer{position:absolute;left:0;top:600px;width:847px;height:385px}
  .offer-copy{
    position:absolute;left:0;top:0;width:215px;height:385px;
    background:linear-gradient(90deg,var(--cream),var(--cream-edge));
    padding:26px 22px 0;text-align:center;
    font-family:"Crimson Text",Georgia,serif;font-style:italic;font-size:16px;line-height:22px;color:var(--cocoa);
  }
  .offer-copy .highlight{
    display:block;margin:14px 0 12px;font-size:32px;line-height:34px;font-weight:700;color:var(--berry-red);
  }
  .offer-photo{
    position:absolute;left:215px;top:0;width:632px;height:385px;
    background:linear-gradient(120deg,#5a3a26 0%,#8fbf5a 20%,#f3e27a 38%,#f7f0c8 52%,#a78a64 62%,#f1c257 78%,#f6f0e2 100%);
  }
  .web-pill{
    position:absolute;left:302px;top:934px;width:456px;height:45px;border-radius:12px;
    background:var(--band-red);color:var(--white);text-align:center;line-height:45px;
    font-style:italic;font-weight:700;font-size:24px;letter-spacing:2px;
  }
  .enquiries{
    position:absolute;left:0;top:985px;width:847px;height:151px;background:var(--mango);
    padding:14px 40px 0;font-size:12.5px;line-height:18px;color:var(--ink);
  }
  .enquiries p{margin-bottom:10px;width:470px}
  .product-photo{
    position:absolute;left:520px;top:958px;width:327px;height:242px;
    background:radial-gradient(ellipse at 70% 35%,#7fd4dc 0%,#5bb6c6 30%,rgba(244,178,28,0) 55%),
               radial-gradient(ellipse at 25% 45%,#ffd23c 0%,#f29a1c 30%,rgba(244,178,28,0) 55%),
               linear-gradient(160deg,rgba(0,0,0,0) 55%,#2c2a2a 75%);
  }
  .address-bar{
    position:absolute;left:0;top:1136px;width:847px;height:64px;background:var(--cocoa-deep);
    color:var(--white);padding:12px 40px 0;font-size:12.5px;line-height:19px;
  }
  .address-bar strong{font-weight:700}
</style>
</head>
<body>
<main class="advert">
  <div class="hero-photo" role="img" aria-label="Close-up of lemon gelato with fresh lemon slices"></div>

  <header class="brand">
    <div class="brand-mark">
      <span class="brand-dot"></span>
      <span class="brand-name">Villa Sorbetto Nero</span>
    </div>
    <p class="brand-tagline">The House of Italian Ice Cream</p>
  </header>

  <h1 class="headline">VILLA SORBETTO NERO</h1>

  <section class="gallery">
    <div class="gallery-photo display-case" role="img" aria-label="Gelato display counter with colourful decorated pans"></div>
    <div class="gallery-photo flavour-pans" role="img" aria-label="Pans of pistachio, lemon and strawberry gelato"></div>
    <div class="gallery-photo scoops" role="img" aria-label="Scoops of orange, pink, green and chocolate gelato with berries"></div>
  </section>

  <h2 class="catering-band">WE ALSO CATER FOR WEDDINGS AND PARTIES</h2>

  <section class="offer">
    <div class="offer-copy">
      Villa Sorbetto Nero has been established for three years and produce artisan gelato from fresh ingredients on a
      <span class="highlight">wholesale scale.</span>
      We supply in scoop cups, ready to scoop pans and can arrange a display freezer of 10 flavours with staff to scoop for guests.
    </div>
    <div class="offer-photo" role="img" aria-label="Display freezer of fruit and cream gelato pans decorated with pineapple, kiwi and orange slices"></div>
  </section>

  <div class="product-photo" role="img" aria-label="Scoops of mango gelato beside a pan of mint-blue gelato"></div>

  <section class="enquiries">
    <p>Villa Sorbetto Nero are versatile in producing flavours to meet your requirements.</p>
    <p>From diabetic gelato to semi-freddo cakes, or just had another flavour in mind?<br>Let us know and we'll do our very best to give you the finest Gelato available.</p>
    <p>For any pre-orders, catering for parties or events, wholesaling, sampling or any other general enquiries and comments please contact us.</p>
  </section>

  <div class="web-pill">www.villasorbettonero.co.uk</div>

  <footer class="address-bar">
    <strong>Villa Sorbetto Nero,</strong> Unit 12 Meridian Trade Park, 48 Fenwick Lane,<br>
    North Ashby, AB4 7QT. <strong>Tel:</strong> 020 71234567, 07700123456, 07700654321
  </footer>
</main>
</body>
</html>
```